Roll Up Banner / Rebranded

Hi. I've been focusing on my branding and seeking to ensure that my name / brand becomes more memorable. As a result I'm looking to update my roll-up banners (2000mm tall, 80mm wide). And have had a look as some basic thoughts. I'll post them here - they need work - but hint at what I am going for. My logo is defined. And I want to have the memorable element / the takeaway that people recall, as being "The Lionel K Revue". I'm "Lionel K" the "V" is just part of my name and need not be emphasised.
The concepts I'll post show the overall vibe - dark background, spare corporate styling. Clean modern concept. The tagline is "high energy comedy hypnosis" The main element is "The Lionel K Revue". Needing a QR near the top for visibility, and my website as a minimum.

Do not add spirals, microphone, faces, watches or other banal hypnosis crap".

Target Market(s)

Corporate events

Industry/Entity Type

Corporate events

Colors
0054AA
0677BA
7BADD7
CADEEF
E8F1F8
0094D4
00A9DD
6FCCEA
C7EBF8
E9F6FB
6B429C
8869AF
B7A5CE
E3DAEB
F3F0F8

Requirements
Must have
• My Logo
Should not have
• Faces, microphones, spirals, watches

```html
<!DOCTYPE html>
<html lang="en">
<head>
<meta charset="utf-8">
<title>The Lionel K Revue – Roll-up Banner</title>
<link rel="stylesheet" href="https://fonts.googleapis.com/css2?family=Anton&family=Josefin+Sans:wght@600;700&family=Great+Vibes&display=swap">
<style>
  :root {
    --page-bg: #d9d9db;
    --banner-black: #0d0d12;
    --stage-blue: #0a2a8c;
    --stage-deep: #07124a;
    --light-blue: #7badd7;
    --white: #ffffff;
    --neon-pink: #f3a6f0;
    --neon-magenta: #d21ee0;
    --url-magenta: #e41fe4;
    --script-pink: #e9b6ee;
  }
  * { margin: 0; padding: 0; box-sizing: border-box; }
  html, body {
    width: 1051px; height: 1200px; overflow: hidden;
    background: var(--page-bg);
  }
  .banner {
    position: absolute; left: 275px; top: 12px;
    width: 500px; height: 1175px;
    background: var(--banner-black);
    overflow: hidden;
  }
  .stage-lights {
    position: absolute; left: 0; top: 0; width: 100%; height: 720px;
    background:
      radial-gradient(ellipse 190px 150px at 50% 90px, rgba(202,222,239,0.75), transparent 70%),
      radial-gradient(ellipse 120px 90px at 78% 330px, rgba(6,119,186,0.45), transparent 70%),
      radial-gradient(ellipse 110px 80px at 20% 450px, rgba(0,84,170,0.35), transparent 70%),
      linear-gradient(180deg, var(--stage-deep) 0%, var(--stage-blue) 30%, #0a1f6e 60%, transparent 100%);
  }
  .brand {
    position: absolute; top: 150px; left: 0; width: 100%;
    display: flex; justify-content: center; align-items: center; gap: 14px;
    font-family: "Josefin Sans", sans-serif; font-weight: 700;
    font-size: 80px; line-height: 1; color: var(--white);
  }
  .brand-dot {
    width: 22px; height: 22px; border-radius: 50%; background: var(--white);
    margin-top: -10px;
  }
  .presents {
    position: absolute; top: 240px; left: 55px; right: 55px;
    display: flex; align-items: center; gap: 18px;
  }
  .presents .rule { flex: 1; height: 2px; background: var(--white); }
  .presents .script {
    font-family: "Great Vibes", cursive; font-size: 48px; color: var(--script-pink);
    line-height: 1;
  }
  .qr-code {
    position: absolute; top: 306px; left: 212px;
    width: 76px; height: 76px;
    background: var(--white);
    border-radius: 4px;
  }
  .show-title {
    position: absolute; left: 68px; top: 409px; width: 372px; height: 326px;
    border: 5px solid var(--neon-pink);
    display: flex; flex-direction: column; align-items: center; justify-content: center;
    font-family: "Anton", sans-serif; color: var(--white); text-align: center;
    text-shadow: 0 0 6px var(--neon-magenta), 0 0 14px var(--neon-magenta), 0 0 26px var(--neon-magenta);
  }
  .show-title .line-small { font-size: 68px; line-height: 1.02; }
  .show-title .line-large { font-size: 84px; line-height: 1.1; }
  .tagline {
    position: absolute; top: 784px; left: 0; width: 100%;
    font-family: "Josefin Sans", sans-serif; font-weight: 700;
    font-size: 48px; line-height: 54px; color: var(--white);
    text-align: center; letter-spacing: 1px;
  }
  .website {
    position: absolute; top: 1110px; left: 0; width: 100%;
    font-family: "Josefin Sans", sans-serif; font-weight: 600;
    font-size: 22px; letter-spacing: 1px; color: var(--url-magenta);
    text-align: center;
  }
</style>
</head>
<body>
  <main class="banner">
    <div class="stage-lights" role="img" aria-label="Row of blue stage spotlights shining down over soft blue bokeh lights"></div>

    <div class="brand"><span>Lionel K</span><span class="brand-dot"></span></div>

    <div class="presents">
      <span class="rule"></span>
      <span class="script">Present</span>
      <span class="rule"></span>
    </div>

    <div class="qr-code" role="img" aria-label="QR code linking to the website"></div>

    <h1 class="show-title">
      <span class="line-small">THE</span>
      <span class="line-large">LIONEL K</span>
      <span class="line-large">REVUE</span>
    </h1>

    <p class="tagline">THE HIGH<br>ENERGY<br>COMEDY<br>HYPNOSIS<br>SHOW</p>

    <p class="website">WWW.LIONELK-REVUE.COM</p>
  </main>
</body>
</html>
```